KRT,LLC

I need a flyer that has my company Logo on it as well as my book cover on it. I need for the flyer to read: "Ashes Under the Bridge" ~ A story of Money,Murder,Sex and family ties in the heart of the city. Read along as Curtis J. Hollow masterfully paint this Wilmington,Delaware tale like no other~The "T.K.V boys" clash in a rain of bullets against North sides own "Zinga boys."
At $14.99 you can own your own copy of "Ashes Under the Bridge."
Contact Curt Hollow @ 302-555-0147 to purchase your paper back copy.
OR
Visit:www.krtllcbooks.example
www.ashezunderthebridge.example
ashesunderthebridge24@mailbox.example
To purchase your order directly off line.
We accept paxo,CoinLeaf and debit cards for those individuals who wish to order on-line!

```html
<!DOCTYPE html>
<html lang="en">
<head>
<meta charset="utf-8">
<title>Ashes Under the Bridge – Flyer</title>
<link rel="stylesheet" href="https://fonts.googleapis.com/css2?family=Arvo:wght@700&family=Poppins:wght@500;600;700&display=swap">
<style>
  :root {
    --page-bg: #e9e6e1;
    --sky-top: #4c6db5;
    --sky-mid: #7f9fd3;
    --sky-low: #d4e2f2;
    --band-red: #c9415c;
    --band-red-dark: #a8304a;
    --price-yellow: #f6c531;
    --grass-top: #7fa25a;
    --grass-bottom: #3f6d2a;
    --footer-red: #e0242c;
    --white: #ffffff;
    --ink: #111111;
  }
  * { box-sizing: border-box; margin: 0; padding: 0; }
  html, body { width: 1200px; height: 1000px; overflow: hidden; background: var(--page-bg); }
  .flyer {
    position: absolute; left: 300px; top: 50px;
    width: 600px; height: 900px; overflow: hidden;
    background: var(--grass-bottom);
    box-shadow: 0 8px 24px rgba(0,0,0,.25);
    font-family: "Poppins", sans-serif; color: var(--white);
  }
  .sky {
    position: absolute; inset: 0 0 auto 0; height: 620px;
    background: linear-gradient(180deg, var(--sky-top) 0%, var(--sky-mid) 40%, var(--sky-low) 75%);
  }
  .title {
    position: absolute; top: 34px; left: 0; width: 100%;
    font-family: "Arvo", serif; font-weight: 700; font-size: 62px; line-height: 1.02;
    text-align: center; text-shadow: 3px 4px 4px rgba(0,0,0,.45);
  }
  .synopsis {
    position: absolute; top: 190px; left: 50px; width: 500px;
    font-size: 16px; line-height: 1.45; text-align: center; font-weight: 500;
    text-shadow: 1px 1px 3px rgba(0,0,0,.55);
  }
  .red-band {
    position: absolute; top: 360px; left: 0; width: 100%; height: 262px;
    background: var(--band-red);
    border-top: 4px solid var(--band-red-dark);
  }
  .price-block { position: absolute; top: 392px; left: 300px; width: 290px; }
  .price {
    font-size: 58px; font-weight: 700; color: var(--price-yellow);
    line-height: 1; text-shadow: 2px 3px 3px rgba(0,0,0,.35);
  }
  .price-note { margin-top: 8px; font-size: 18px; font-weight: 600; line-height: 1.3; }
  .book-cover {
    position: absolute; top: 330px; left: 28px; width: 250px; height: 330px;
    background: linear-gradient(160deg, #b44054 0%, #7a6a6a 45%, #1b2a9c 100%);
    border: 6px solid #1f2fd6;
    box-shadow: 6px 8px 12px rgba(0,0,0,.4);
  }
  .photo-strip {
    position: absolute; top: 560px; left: 290px; width: 310px; height: 100px;
    background: linear-gradient(90deg, #6b5a4a, #a79a8c 35%, #4a3f3a 65%, #b89a88);
  }
  .lawn {
    position: absolute; top: 620px; left: 0; width: 100%; height: 230px;
    background: linear-gradient(180deg, var(--grass-top), var(--grass-bottom));
  }
  .contact {
    position: absolute; top: 680px; left: 190px; width: 270px;
    font-size: 12px; line-height: 1.45; text-align: center;
    text-shadow: 1px 1px 2px rgba(0,0,0,.5);
  }
  .contact .links { margin-top: 8px; font-size: 13px; font-weight: 600; }
  .contact .email { margin-top: 4px; font-size: 11px; font-weight: 500; }
  .brand {
    position: absolute; top: 770px; left: 470px;
    display: flex; align-items: center; gap: 8px;
  }
  .brand-dot { width: 40px; height: 40px; border-radius: 50%; background: var(--ink); border: 3px solid var(--white); flex: none; }
  .brand-name { font-size: 16px; font-weight: 700; color: var(--white); white-space: nowrap; }
  .footer {
    position: absolute; bottom: 0; left: 0; width: 100%; height: 50px;
    background: var(--footer-red);
    display: flex; align-items: center; justify-content: center;
    font-size: 12px; font-weight: 600; white-space: nowrap;
  }
</style>
</head>
<body>
  <main class="flyer">
    <div class="sky"></div>
    <h1 class="title">"Ashes Under<br>the Bridge"</h1>
    <p class="synopsis">A story of Money, Murder, Sex and family ties in the heart of the city. Read along as Curtis J. Hollow masterfully paint this Wilmington, Delaware tale like no other~The "T.K.V boys" clash in a rain of bullets against North sides own "Zinga boys."</p>

    <div class="red-band"></div>
    <div class="price-block">
      <div class="price">At $14.99</div>
      <p class="price-note">you can own your own copy of "Ashes Under the Bridge."</p>
    </div>

    <div class="lawn"></div>
    <div class="photo-strip" role="img" aria-label="Strip of scene photographs from the story"></div>
    <div class="book-cover" role="img" aria-label="Book cover of Ashes Under the Bridge with the author standing in front of a brick building"></div>

    <div class="contact">
      <p>Contact Curt Hollow @ 302-555-0147<br>to purchase your paper back copy.<br>or visit</p>
      <p class="links">www.krtllcbooks.example<br>www.ashezunderthebridge.example</p>
      <p class="email">ashesunderthebridge24@mailbox.example</p>
    </div>

    <div class="brand">
      <span class="brand-dot"></span>
      <span class="brand-name">KRT,LLC</span>
    </div>

    <footer class="footer">We accept paxo, CoinLeaf and Debit Cards for those individuals who wish to order on-line!</footer>
  </main>
</body>
</html>
```